Harvest Gathering event flyer

I would like a church event flyer designed. The event is called "HARVEST GATHERING 2018". I am looking for a professional, yet catchy design that uses our brand colors and logo creatively while communicating key information of the event effectively.

1. The logo is attached in two color formats. The designer has the choice to use them as he/she want.

2. The location of the event is: Lindqvist Community Center, 482 Tamsworth Street, Portland, ME 04102
3. Time and date of event. The designer can organize and format the date and time as he/she pleases.
December 28th, 29th @ 7:00PM
December 30th @ 10:00AM
4. The topic of the event is "Tongues of fire". The designer is free to use this phrase as he/she pleases to create a good composition.
5. Speaker: Prophet Marcus Obuya
6. Contact information: contact@cedarbrookfellowship.org - Telephone number: 207 555 0148

7. I would also like the following three words on the flyer. These words describe the focus of the event: FIRE, REVIVAL, PROPHETIC

```html
<!DOCTYPE html>
<html lang="en">
<head>
<meta charset="utf-8">
<title>Harvest Gathering 2018 – Tongues of Fire</title>
<link rel="stylesheet" href="https://fonts.googleapis.com/css2?family=Alfa+Slab+One&family=Smokum&family=Black+Ops+One&family=Arimo:ital,wght@0,700;1,700&display=swap">
<style>
  :root {
    --rust: #9e5439;
    --rust-dark: #8b4a44;
    --plum: #5f4a57;
    --steel: #2c5672;
    --navy: #14375b;
    --orange: #f7941d;
    --white: #ffffff;
    --dove-grey: #8f9bb8;
  }
  * { margin: 0; padding: 0; box-sizing: border-box; }
  html, body { width: 848px; height: 1200px; overflow: hidden; background: var(--rust); }
  .flyer { position: relative; width: 848px; height: 1200px; overflow: hidden; background: var(--rust); }
  .backdrop { position: absolute; inset: 0; }
  .flames {
    position: absolute; left: 0; top: 560px; width: 848px; height: 640px;
    background:
      radial-gradient(ellipse 60% 40% at 50% 95%, rgba(255,140,40,.85), transparent 70%),
      radial-gradient(ellipse 40% 30% at 20% 70%, rgba(230,100,30,.7), transparent 70%),
      radial-gradient(ellipse 40% 30% at 80% 75%, rgba(220,90,40,.65), transparent 70%),
      linear-gradient(to bottom, rgba(120,70,70,0) 0%, rgba(140,70,50,.6) 25%, #7a3622 55%, #3a1c18 100%);
  }
  .dove-large { position: absolute; left: 0; top: 40px; width: 190px; height: 370px;
    background: linear-gradient(160deg, #ffffff, #f1f1f1); border-radius: 50% 40% 45% 55%;
    opacity: .95; }
  .dove-small { position: absolute; left: 350px; top: 415px; width: 130px; height: 140px;
    background: var(--dove-grey); border-radius: 50%; opacity: .9; }
  .brand { position: absolute; left: 195px; top: 88px; width: 455px;
    display: flex; justify-content: center; align-items: center; gap: 12px; white-space: nowrap; }
  .brand-dot { width: 18px; height: 18px; border-radius: 50%; background: var(--white); }
  .brand-name { font-family: "Alfa Slab One", serif; font-size: 40px; color: var(--white); letter-spacing: 1px; }
  .focus { position: absolute; font-family: "Alfa Slab One", serif; color: var(--orange);
    font-size: 51px; line-height: 1; white-space: nowrap; }
  .focus-fire { left: 354px; top: 312px; }
  .focus-revival { left: 75px; top: 444px; }
  .focus-prophetic { left: 486px; top: 444px; }
  .topic { position: absolute; left: 0; top: 580px; width: 848px; height: 130px; overflow: visible; }
  .topic-text { font-family: "Smokum", "Rye", serif; font-size: 104px; fill: var(--white); }
  .speaker { position: absolute; left: 0; width: 848px; top: 728px; text-align: center; white-space: nowrap;
    font-family: "Alfa Slab One", serif; font-size: 36px; line-height: 1.2; color: var(--navy); }
  .contact { position: absolute; left: 0; width: 848px; top: 833px; text-align: center; white-space: nowrap;
    font-family: "Arimo", Arial, sans-serif; font-weight: 700; font-size: 17px; color: var(--white); line-height: 34px; }
  .event-name { position: absolute; left: 0; width: 848px; top: 998px; text-align: center; white-space: nowrap;
    font-family: "Black Ops One", sans-serif; font-size: 40px; line-height: 1.2; color: var(--navy); letter-spacing: 5px; }
  .schedule { position: absolute; left: 0; width: 848px; top: 1062px; text-align: center; white-space: nowrap;
    font-family: "Arimo", Arial, sans-serif; font-style: italic; font-weight: 700; font-size: 30px; color: var(--white); line-height: 36px; }
</style>
</head>
<body>
<main class="flyer">
  <svg class="backdrop" width="848" height="1200" viewBox="0 0 848 1200" aria-hidden="true">
    <rect x="0" y="0" width="848" height="1200" fill="var(--rust)"/>
    <rect x="560" y="0" width="90" height="1200" fill="var(--rust-dark)"/>
    <rect x="650" y="0" width="88" height="1200" fill="var(--plum)"/>
    <rect x="738" y="0" width="110" height="1200" fill="var(--steel)"/>
    <rect x="195" y="0" width="457" height="292" fill="var(--navy)"/>
    <rect x="199" y="0" width="82" height="282" fill="var(--rust)"/>
    <rect x="565" y="0" width="82" height="282" fill="var(--rust-dark)"/>
    <rect x="336" y="290" width="170" height="120" fill="var(--navy)"/>
    <rect x="0" y="400" width="738" height="148" fill="var(--navy)"/>
    <rect x="336" y="548" width="170" height="652" fill="var(--navy)" opacity="0.75"/>
  </svg>
  <div class="flames" role="img" aria-label="Photograph of glowing orange fire flames"></div>
  <div class="dove-large" role="img" aria-label="Illustration of a white dove in flight"></div>
  <div class="dove-small" role="img" aria-label="Small illustration of a descending grey dove"></div>

  <div class="brand">
    <span class="brand-dot"></span>
    <span class="brand-name">CEDARBROOK</span>
  </div>

  <div class="focus focus-fire">FIRE</div>
  <div class="focus focus-revival">REVIVAL</div>
  <div class="focus focus-prophetic">PROPHETIC</div>

  <svg class="topic" width="848" height="130" viewBox="0 0 848 130" role="heading" aria-level="1">
    <text class="topic-text" x="68" y="110" textLength="712" lengthAdjust="spacingAndGlyphs">TONGUES OF FIRE</text>
  </svg>
  <p class="speaker">Speaker: Prophet Marcus Obuya</p>

  <div class="contact">
    <p>Contact information: contact@cedarbrookfellowship.org</p>
    <p>Telephone number: 207 555 0148</p>
    <p>Location: Lindqvist Community Center, 482 Tamsworth Street, Portland, ME 04102</p>
  </div>

  <h2 class="event-name">HARVEST GATHERING 2018</h2>
  <div class="schedule">
    <p>December 28th, 29th @ 7:00PM</p>
    <p>December 30th @ 10:00AM</p>
  </div>
</main>
</body>
</html>
```